Small Machinery Hire Company Needs Coaster Design

Please design an eye catching coaster/sticker to place in local pubs and restaurants. Please use our attached logo and incorporate our rustic earthy feel into the colours. Use the following details. Definite want the focus to be on the logo and phone number.

Would appreciate if it could be multi-purpose as a basic sign as well.

Dry/Wet Hire Available
Ph: 0471629058

(Use FaceBook icon) facebook.com/bramwellkestrelplant2917/

Target Market(s)

At homer DIY-ers. Middle class men who would like to hire a machine to work on their own pride and joy home.

Industry/Entity Type

Construction Company

Font styles to use
Other font styles liked:
• Something that matches the Logo

Colors
fefdec
ec1f27
474747
919191

Requirements
Nice to have
• Preferably a square shape so the it is more multi purpose

```html
<!DOCTYPE html>
<html lang="en">
<head>
<meta charset="utf-8">
<title>Bramwell Kestrel Plant – Coaster</title>
<link rel="stylesheet" href="https://fonts.googleapis.com/css2?family=Rye&family=Graduate&display=swap">
<style>
  :root {
    --backdrop: #3b3836;
    --rust-red: #9e1c18;
    --deep-black: #050505;
    --cream: #fefdec;
  }
  * { margin: 0; padding: 0; box-sizing: border-box; }
  html, body {
    width: 1200px;
    height: 1000px;
    overflow: hidden;
    background: var(--backdrop);
  }
  .canvas {
    position: relative;
    width: 1200px;
    height: 1000px;
  }
  .coaster {
    position: absolute;
    left: 190px;
    top: 90px;
    width: 820px;
    height: 820px;
    overflow: hidden;
    background: linear-gradient(to bottom,
      var(--rust-red) 0%,
      var(--rust-red) 62%,
      #5a1210 70%,
      var(--deep-black) 79%,
      var(--deep-black) 100%);
    color: var(--cream);
  }
  .brand-name {
    position: absolute;
    top: 90px;
    left: 0;
    width: 100%;
    text-align: center;
    font-family: "Rye", serif;
    font-size: 84px;
    line-height: 1.12;
    color: var(--cream);
  }
  .hire-tagline {
    position: absolute;
    top: 440px;
    left: 0;
    width: 100%;
    text-align: center;
    font-family: "Graduate", serif;
    font-size: 46px;
    letter-spacing: 5px;
    color: var(--cream);
  }
  .contact-row {
    position: absolute;
    left: 48px;
    right: 40px;
    display: flex;
    align-items: center;
    gap: 30px;
    font-family: "Graduate", serif;
    color: var(--cream);
    white-space: nowrap;
  }
  .contact-row.phone { top: 585px; font-size: 56px; letter-spacing: 3px; }
  .contact-row.social { top: 712px; font-size: 30px; letter-spacing: 1px; }
  .contact-icon { width: 72px; height: 72px; flex: none; }
  .social-square {
    width: 68px;
    height: 68px;
    flex: none;
    background: var(--cream);
    border-radius: 4px;
  }
</style>
</head>
<body>
<main class="canvas">
  <section class="coaster">
    <div class="brand-name">BRAMWELL<br>KESTREL PLANT</div>
    <div class="hire-tagline">Dry/Wet Hire Available</div>

    <div class="contact-row phone">
      <svg class="contact-icon" viewBox="0 0 24 24" aria-hidden="true">
        <path fill="#fefdec" d="M6.6 2.2c.6-.4 1.4-.3 1.8.3l2.2 3.3c.4.6.3 1.3-.2 1.8L8.9 9c1.1 2.4 3.2 4.6 5.8 5.9l1.5-1.5c.5-.5 1.3-.6 1.8-.2l3.3 2.2c.6.4.7 1.2.3 1.8l-1.4 2.1c-.6.9-1.7 1.3-2.8 1C10.9 18.4 5.4 12.9 3.5 6.4c-.3-1.1.1-2.2 1-2.8z"/>
      </svg>
      <span class="contact-text">0471629058</span>
    </div>

    <div class="contact-row social">
      <span class="social-square" aria-hidden="true"></span>
      <span class="contact-text">/bramwellkestrelplant2917</span>
    </div>
  </section>
</main>
</body>
</html>
```